New Website Design (Uncoded) Competition for Velto Trade Link

Please submit design concepts for a Joomla 3.0 Website for VELTO TRADE LINK company. Our client prefers a modem style design, responsive to all mobile devices,
The website demo content needs to be clear and detailed.

Menu sample:
Home/About Us/Service/Strength/Partner/News/Contact US/Blog

Requirements:
1. Only need to submit the PSD for the design, coding work is not included.
2. Please submit both Homepage and Inner page to demonstrate the concept.
3. The Homepage needs to include: LOGO/MENU/Banner/Language Switcher/Company Introduction/Welcome module/Advertising Module/Footer Menu/Footer/Copyright/Social Links
4. Use Asian business women for demo pictures/Could try city pictures for background.
5. Prefer SINGLE SCREEN design rather than scrollable multiple screen designs.
6. Avoid any chain symbol since the company is more about financial business.
7. Avoid any direct connotations related with money or cash.
Updates

Hi Designers, I have clearly state the requirements that avoid using neg connontation pictures like cash/ property, though still receive concepts like that. Please check the brief clearly and mark at Update with "cheers" Kip from LW

Target Market(s)

Shenzhen Dorvik Velto Trade link Company provide cross-border Supply chain Financial service by integrating Dorvik Trade Link resource.
The Company mission is become the most respectful, professional and valuable Chinese Supply Chain Financial Company, pioneer the supply chain industry.

Industry/Entity Type

Financial

Font styles to use
Sans Serif

Colors
33b7a4

Requirements
Must have
• 1. Necessary Web element, including Logo/navigation/ Banner/ Footer
2. Asia business Women pictures.
Should not have
• 6. Avoid any chain symbol since the company is more about financial business.

```html
<!DOCTYPE html>
<html lang="en">
<head>
<meta charset="utf-8">
<title>Velto Trade Link</title>
<link href="https://fonts.googleapis.com/css2?family=Lato:ital,wght@0,300;0,400;0,700;1,400&display=swap" rel="stylesheet">
<style>
:root{
  --teal:#33b7a4;
  --teal-dark:#2a9d8c;
  --ink:#333;
  --muted:#555;
  --footer:#5d5d5d;
  --footer-deep:#4b4b4b;
  --line:#e6e6e6;
  --card:#fbfbfb;
}
*{margin:0;padding:0;box-sizing:border-box}
html,body{width:960px;height:1200px;overflow:hidden}
body{font-family:'Lato',sans-serif;color:var(--ink);background:#fff;position:relative}
a{color:inherit;text-decoration:none}
.abs{position:absolute}

.topbar{position:absolute;left:0;top:0;width:960px;height:28px;background:var(--teal);color:#fff}
.lang{left:102px;top:7px;font-size:9.5px;font-weight:700}
.lang svg{vertical-align:middle;margin-left:4px}
.social-top{right:102px;top:8px;display:flex;gap:6px}
.social-top span{width:12px;height:12px;border-radius:50%;background:rgba(255,255,255,.9)}

.header{position:absolute;left:0;top:28px;width:960px;height:58px;background:#fff}
.brand{left:104px;top:14px;display:flex;align-items:center;gap:8px}
.brand-mark{width:26px;height:26px;border-radius:50%;background:var(--teal)}
.brand-name{font-size:17px;font-weight:700;color:#555;letter-spacing:.5px;line-height:1}
.nav{top:23px;font-size:10.5px;font-weight:700;color:#333}
.nav a{position:absolute;white-space:nowrap}

.hero{position:absolute;left:0;top:86px;width:960px;height:364px;
  background:linear-gradient(180deg,#4fbfae 0%,#3aa797 45%,#2f9888 100%)}
.hero-title{left:101px;top:58px;font-size:47px;font-weight:300;color:#fff;line-height:52px}
.hero-sub{left:101px;top:170px;font-size:16px;color:#1c2b2a;line-height:26px}
.btn-start{left:102px;top:246px;width:110px;height:32px;background:#555;color:#fff;font-size:9.5px;font-weight:700;display:flex;align-items:center;justify-content:center}
.hero-photo{left:470px;top:61px;width:388px;height:211px;background:linear-gradient(120deg,#dfe3e1 0%,#c9cfcc 50%,#b4bbb8 100%)}
.pager{left:422px;top:320px;width:116px;height:32px;border-radius:16px;background:rgba(60,110,105,.45);display:flex;align-items:center;justify-content:center;gap:6px}
.pager span{width:20px;height:20px;border-radius:50%;border:1px solid #fff;color:#fff;font-size:10px;display:flex;align-items:center;justify-content:center}
.pager .on{background:#fff;color:#333;width:23px;height:23px}

.welcome-title{left:0;top:476px;width:960px;text-align:center;font-size:19.5px;font-weight:700}
.welcome-title em{font-style:normal;color:var(--teal)}
.intro{left:114px;top:523px;width:732px;text-align:center;font-size:10.1px;line-height:14.3px;color:#555;letter-spacing:-.05px}

.card{position:absolute;top:641px;width:227px;height:183px;background:var(--card);border:1px solid var(--line);text-align:center}
.card-icon{position:absolute;top:610px;width:61px;height:61px;border-radius:50%;background:var(--teal);display:flex;align-items:center;justify-content:center}
.card-icon.alt{background:#555;border:3px solid var(--teal);width:67px;height:67px;top:607px}
.card h3{position:absolute;top:50px;width:100%;font-size:12px;font-weight:400;color:#333}
.card p{position:absolute;top:74px;width:100%;font-size:8.3px;line-height:15px;color:#555}
.card .more{position:absolute;left:70px;top:127px;width:86px;height:25px;border:1px solid #ddd;background:#fff;font-size:8.5px;font-weight:700;display:flex;align-items:center;justify-content:center}
.card .more.solid{background:var(--teal);border-color:var(--teal);color:#fff}

.ad{left:245px;top:853px;width:470px;height:57px;background:#e0e0e0;color:#a9b3bb;font-size:32px;font-weight:700;display:flex;align-items:center;justify-content:center}

.footer{position:absolute;left:0;top:939px;width:960px;height:209px;background:var(--footer);color:#fff}
.f-head{font-size:14.5px;font-weight:300}
.follow{position:absolute;display:flex;gap:7px;align-items:flex-start}
.follow i{width:19px;height:19px;display:block}
.follow b{display:block;font-size:10px;font-weight:700;color:#ccc;line-height:12px}
.follow small{display:block;font-size:7.5px;color:#bbb;line-height:10px}
.links{position:absolute;list-style:none}
.links li{width:174px;height:26px;border-bottom:1px solid #777;font-size:8.8px;padding-top:7px;padding-left:11px;position:relative}
.links li:last-child{border-bottom:none}
.links li::before{content:"";position:absolute;left:0;top:10px;width:4px;height:4px;background:var(--teal)}
.links li.hl{color:var(--teal)}
.email{left:684px;top:53px;width:150px;height:26px;background:#eee;border:1px solid var(--teal);font-size:9px;font-style:italic;color:#aaa;padding:8px 13px}
.email-go{left:834px;top:53px;width:24px;height:26px;background:var(--teal);display:flex;align-items:center;justify-content:center}

.bottombar{position:absolute;left:0;top:1148px;width:960px;height:52px;background:var(--footer-deep);color:#fff;font-size:9px}
.bottombar .copy{left:103px;top:21px}
.bottombar .copy em{font-style:normal;color:var(--teal)}
.bottombar a{position:absolute;top:21px}
</style>
</head>
<body>

<div class="topbar">
  <div class="abs lang">Choose Your Languages<svg width="7" height="5" viewBox="0 0 7 5"><path d="M1 1l2.5 2.5L6 1" stroke="#fff" stroke-width="1.4" fill="none"/></svg></div>
  <div class="abs social-top"><span></span><span></span><span></span><span></span><span></span><span></span><span></span><span></span></div>
</div>

<header class="header">
  <div class="abs brand"><span class="brand-mark"></span><span class="brand-name">Velto Trade Link</span></div>
  <nav class="abs nav" style="left:0;width:960px">
    <a style="left:292px">HOME</a><a style="left:348px">ABOUT US</a><a style="left:422px">SERVICE</a><a style="left:490px">STRENGTH</a><a style="left:566px">PARTNER</a><a style="left:636px">SALE OFF</a><a style="left:706px">NEWS</a><a style="left:760px">BLOG</a><a style="left:812px">CONTACT</a>
  </nav>
</header>

<section class="hero" role="img" aria-label="City skyline at dusk under a teal tint">
  <h1 class="abs hero-title">Feeling the life<br>in a way different</h1>
  <p class="abs hero-sub">My dream is to change the world.<br>It sounds hard to believe but nothing is impossible.</p>
  <a class="abs btn-start">GET STARTED NOW</a>
  <div class="abs hero-photo" role="img" aria-label="Asian business woman smiling in a bright office with two colleagues talking behind her"></div>
  <div class="abs pager"><span>1</span><span class="on">2</span><span>3</span><span>4</span></div>
</section>

<h2 class="abs welcome-title"><em>WELCOME TO</em> VELTO TRADE LINK</h2>
<p class="abs intro">It is a long established fact that a reader will be distracted by the readable content of a page when looking at its layout. The point of using Lorem Ipsum is that it has a more-or-less normal distribution of letters, as opposed to using 'Content here, content here', making it look like readable English. Many desktop publishing packages and web page editors now use Lorem Ipsum as their default model text, and a search for 'lorem ipsum' will uncover many web sites still in their infancy. Various versions have evolved over the years, sometimes by accident, sometimes on purpose (injected humour and the like)</p>

<div class="card" style="left:122px"><h3>Strategic Vision</h3><p>Praesent turpis mauris, aliquet id dolor<br>Gravida adipiscing lectus ut rutrum<br>Aenean at posuere risus.</p><a class="more">Read More</a></div>
<div class="card" style="left:366px"><h3>Excellent Team</h3><p>Praesent turpis mauris, aliquet id dolor<br>Gravida adipiscing lectus ut rutrum<br>Aenean at posuere risus.</p><a class="more solid">Read More</a></div>
<div class="card" style="left:612px"><h3>Winner</h3><p>Praesent turpis mauris, aliquet id dolor<br>Gravida adipiscing lectus ut rutrum<br>Aenean at posuere risus.</p><a class="more">Read More</a></div>

<div class="card-icon" style="left:204px"><svg width="20" height="14" viewBox="0 0 20 14"><circle cx="5" cy="9" r="4" fill="none" stroke="#fff" stroke-width="2"/><circle cx="15" cy="9" r="4" fill="none" stroke="#fff" stroke-width="2"/><rect x="7" y="2" width="6" height="5" fill="#fff"/></svg></div>
<div class="card-icon alt" style="left:446px"><svg width="20" height="16" viewBox="0 0 20 16"><path d="M4 1h12l3 4-9 10L1 5z M1 5h18 M7 1l3 14 3-14" fill="none" stroke="var(--teal)" stroke-width="1.3"/></svg></div>
<div class="card-icon" style="left:694px"><svg width="18" height="18" viewBox="0 0 18 18"><path d="M4 1h10v5a5 5 0 0 1-10 0z M4 3H1v2a3 3 0 0 0 3 3 M14 3h3v2a3 3 0 0 1-3 3 M9 11v3 M5 17h8v-2H5z" fill="#fff" stroke="#fff" stroke-width="1.2"/></svg></div>

<div class="abs ad">728 X90 Banner</div>

<footer class="footer">
  <h4 class="abs f-head" style="left:102px;top:15px">Connect With Us</h4>
  <div class="follow" style="left:102px;top:50px"><i style="background:#f5a623"></i><div><b>Subscribe</b><small>to RSS Feed</small></div></div>
  <div class="follow" style="left:190px;top:50px"><i style="background:#29a9e0"></i><div><b>Follow Us</b><small>on Chirpline</small></div></div>
  <div class="follow" style="left:102px;top:89px"><i style="background:#3b64b5"></i><div><b>Find Us</b><small>on Hallway</small></div></div>
  <div class="follow" style="left:190px;top:89px"><i style="background:#6cb52d"></i><div><b>Find Us</b><small>on Circleplus</small></div></div>
  <div class="follow" style="left:102px;top:128px"><i style="background:#e0452b"></i><div><b>Follow Us</b><small>on Corkboard</small></div></div>
  <div class="follow" style="left:190px;top:128px"><i style="background:#c93a8e"></i><div><b>Follow Us</b><small>on Shotcase.</small></div></div>

  <h4 class="abs f-head" style="left:306px;top:15px">Useful Links</h4>
  <ul class="links" style="left:306px;top:44px"><li>Home</li><li class="hl">About Us</li><li>Services</li><li>Strength</li><li>Partner</li><li>News</li></ul>
  <ul class="links" style="left:490px;top:44px"><li style="border-bottom:1px solid #777">Contact US</li><li class="hl">Help Center</li><li style="border-bottom:1px solid #777">Blog</li></ul>

  <h4 class="abs f-head" style="left:684px;top:17px">News Letter Widget</h4>
  <div class="abs email">Your email here</div>
  <div class="abs email-go"><svg width="10" height="6" viewBox="0 0 10 6"><path d="M0 3h9M6 0.5L9 3 6 5.5" stroke="#fff" fill="none"/></svg></div>
</footer>

<div class="bottombar">
  <div class="abs copy">Copyright 2014 <em>VELTO TRADE LINK</em> &nbsp;| &nbsp;All Rights Reserved</div>
  <a style="left:402px">Home</a><a style="left:450px">About Us</a><a style="left:512px">Service</a><a style="left:567px">Strength</a><a style="left:626px">Partner</a><a style="left:681px">Sale Off</a><a style="left:737px">News</a><a style="left:784px">Blog</a><a style="left:826px">Contact</a>
</div>

</body>
</html>
```